Website for Velmorund Capital, my new firm that raises money from investors to buy, build, own an...

Velmorund Capital needs a website! We are a new company with very experienced people, who invest in, own and build hotel properties, as well as apartments and other commercial real estate. We seek investors for our projects, and we provide safe, secure returns on their investment in our projects. Our new logo is designed to exhibit strength, class and security, and would like our website to continue on this theme. Our name, Velmorund, is a word-play on a Greek word “aristeia”, which means “excellence” and “a warriors finest moment of glory in war”. If you are in business, you realize that much of it is like war, with strategy and moves and opponents and competitors, and ever-changing economic conditions and threats that make business very much like war. We like to think that we are good at business (war), and so have named our company “Velmorund”, using the founders last name and the word “aristeia” combined. Another definition of "aristeia" is "performing at the peak of one's potential after a long struggle"...again, much like business in real life! The website design should exhibit financial security, smart moves, and positive growth towards a bright future.

Target Market(s)

The target market is smart and wealthy investors, with others such as brokers, cities and government agencies, lenders, sellers, partners, etc also looking at it.

Industry/Entity Type

Investment

Number of Pages Required

5+ page

Font styles to use
Sans Serif

Colors
fec214

Requirements
Must have
• Our website should have a landing page, a "about" or bio page, a projects page and a contact us page. Our new logo uses the colors black and gold, so this should be factored in to our site. The site should be simple, yet impactful and impressive. I have actually two logos, which can be mixed and interchanged in a complimentary way, each with their own unique look.
Nice to have
• I have uploaded a couple screenshots of a website i like, and the simplicity I mention.
Should not have
• The site should not be flashy or complicated or complex or "busy"

```html
<!DOCTYPE html>
<html lang="en">
<head>
<meta charset="utf-8">
<title>Velmorund Capital</title>
<link rel="stylesheet" href="https://fonts.googleapis.com/css2?family=Poppins:wght@400;500;600&family=Josefin+Sans:wght@600;700&family=Great+Vibes&display=swap">
<style>
:root{
  --gold:#fec214;
  --ink:#111111;
  --night:#1f2833;
  --paper:#f2f2f2;
  --text:#7a7a7a;
  --white:#ffffff;
}
*{box-sizing:border-box;margin:0;padding:0}
html,body{width:1200px;height:2429px;overflow:hidden}
body{position:relative;font-family:'Poppins',sans-serif;color:var(--ink);background:var(--white)}
.abs{position:absolute}

/* Hero */
.hero{position:absolute;left:0;top:0;width:1200px;height:700px;
  background:linear-gradient(160deg,#3a4450 0%,#252c35 45%,#151a20 100%)}
.hero-wave{position:absolute;left:0;top:672px;width:1200px;height:40px}
.brand{position:absolute;left:86px;top:60px;display:flex;align-items:center;gap:12px;
  font-family:'Poppins',sans-serif;font-weight:600;font-size:26px;color:var(--white);letter-spacing:1px}
.brand-mark{width:18px;height:18px;background:var(--gold)}
.nav{position:absolute;top:46px;left:610px;display:flex;gap:0}
.nav a{position:absolute;font-size:18px;font-weight:500;color:var(--white);text-decoration:none;white-space:nowrap}
.nav a.active{color:var(--gold)}
.search{position:absolute;left:1092px;top:52px}
.hero-title{position:absolute;left:0;width:1200px;top:272px;text-align:center;
  font-family:'Great Vibes',cursive;font-size:72px;color:var(--white);font-weight:400}
.hero-sub{position:absolute;left:270px;width:660px;top:370px;text-align:center;
  font-size:20px;line-height:36px;color:var(--white)}
.btn{position:absolute;background:var(--gold);color:var(--ink);font-weight:600;
  display:flex;align-items:center;justify-content:center;text-decoration:none}
.dots{position:absolute;left:1150px;top:306px}
.dot{width:11px;height:11px;border:1.5px solid #c9c9c9;border-radius:50%;margin-bottom:10px}
.dot.on{background:var(--white);border-color:var(--white)}

/* About */
.about{position:absolute;left:0;top:700px;width:1200px;height:490px;background:var(--paper)}
.section-title{position:absolute;font-family:'Josefin Sans',sans-serif;font-weight:600;font-size:40px;color:var(--ink)}
.title-rule{position:absolute;height:4px;width:72px;background:var(--ink)}
.about-text{position:absolute;left:655px;top:172px;width:450px;font-size:15px;line-height:26.5px;color:var(--text)}
.photo{position:absolute}

/* Projects */
.filters .filter{position:absolute;left:82px;width:124px;height:49px;padding-left:13px;
  display:flex;align-items:center;font-size:20px;color:#555}
.filters .filter.active{background:var(--gold);color:var(--ink);font-weight:500}

/* Quote */
.quote{position:absolute;left:0;top:1768px;width:1200px;height:338px;
  background:linear-gradient(180deg,#2b2f33 0%,#1f2a33 55%,#1a2630 100%)}
.quote h2{position:absolute;left:0;width:1200px;top:52px;text-align:center;
  font-family:'Josefin Sans',sans-serif;font-weight:600;font-size:40px;color:var(--white)}
.quote p{position:absolute;left:200px;width:800px;top:124px;text-align:center;font-size:22px;line-height:40px;color:var(--white)}

/* Footer */
.footer{position:absolute;left:0;top:2106px;width:1200px;height:264px;background:var(--ink);color:var(--white)}
.footer h3{position:absolute;font-size:20px;font-weight:600}
.footer .item{position:absolute;font-size:15px;line-height:28px;white-space:nowrap}
.footer-brand{position:absolute;left:90px;top:112px;display:flex;align-items:center;gap:12px;
  font-weight:600;font-size:30px;letter-spacing:1px}
.news-text{position:absolute;left:846px;top:82px;width:290px;font-size:15px;line-height:27px}
.news-input{position:absolute;left:846px;top:2290px;width:231px;height:38px;background:var(--white);
  font-size:12px;color:#999;padding-left:12px;display:flex;align-items:center}
.bottom-bar{position:absolute;left:0;top:2370px;width:1200px;height:59px;background:var(--gold)}
.copyright{position:absolute;left:82px;top:18px;font-size:15px;color:var(--ink)}
.social{position:absolute;top:16px;width:28px;height:28px;border-radius:50%;background:#333}
</style>
</head>
<body>

<header class="hero" role="img" aria-label="Modern apartment building with glass balconies at dusk">
</header>
<svg class="hero-wave" viewBox="0 0 1200 40" aria-hidden="true">
  <path d="M0 18 Q30 8 60 16 T120 14 T180 18 T240 12 T300 17 T360 13 T420 18 T480 12 T540 16 T600 14 L600 40 L0 40Z" fill="#f2f2f2"/>
  <path d="M600 14 Q630 10 660 16 T720 12 T780 17 T840 13 T900 18 T960 12 T1020 16 T1080 13 T1140 17 T1200 10 L1200 40 L600 40Z" fill="#f2f2f2"/>
  <path d="M634 22 A22 22 0 0 0 678 22 Z" fill="#151a20"/>
</svg>

<div class="brand"><span class="brand-mark"></span>Velmorund Capital</div>
<nav class="nav">
  <a class="active" style="left:0">Home</a>
  <a style="left:98px">About Us</a>
  <a style="left:223px">Projects</a>
  <a style="left:340px">Contact Us</a>
</nav>
<svg class="search" width="16" height="16" viewBox="0 0 16 16" aria-hidden="true">
  <circle cx="6.5" cy="6.5" r="4.5" fill="none" stroke="#fec214" stroke-width="2"/>
  <line x1="10" y1="10" x2="14" y2="14" stroke="#fec214" stroke-width="2.2"/>
</svg>

<h1 class="hero-title">Welcome to Velmorund Capital</h1>
<p class="hero-sub">Lorem ipsum dolor sit amet, consectetur adipiscing elit, sed do eiusmod tempor incididunt ut labore et</p>
<a class="btn" style="left:489px;top:455px;width:222px;height:60px;font-size:20px">Get Started</a>
<div class="dots"><div class="dot"></div><div class="dot on"></div><div class="dot"></div><div class="dot"></div><div class="dot"></div></div>

<section class="about">
  <svg class="abs" style="left:80px;top:73px" width="280" height="368" aria-hidden="true">
    <polygon points="0,0 278,0 250,28 28,28 28,340 250,340 222,368 0,368" fill="#fec214"/>
  </svg>
  <div class="photo" style="left:108px;top:98px;width:465px;height:318px;background:linear-gradient(135deg,#2d3440 0%,#dfe6ee 45%,#f4f6f8 70%,#c8d2de 100%)"
       role="img" aria-label="Business people reviewing financial charts with a tablet"></div>
  <h2 class="section-title" style="left:655px;top:95px">About Us</h2>
  <div class="title-rule" style="left:655px;top:150px"></div>
  <p class="about-text">Lorem ipsum dolor sit amet, consectetur adipiscing elit, sed do eiusmod tempor incididunt ut labore et dolore magna aliqua. Ut enim ad minim veniam, quis nostrud exercitation ullamco laboris nisi ut aliquip ex ea commodo consequat. Duis aute irure dolor in reprehenderit in voluptate velit esse cillum dolore eu fugiat nulla pariatur.</p>
  <a class="btn" style="left:655px;top:355px;width:161px;height:52px;font-size:18px">Read More</a>
</section>

<section class="projects">
  <h2 class="section-title" style="left:312px;top:1224px">Projects</h2>
  <div class="title-rule" style="left:312px;top:1288px"></div>
  <div class="filters">
    <div class="filter active" style="top:1318px">All</div>
    <div class="filter" style="top:1390px">Apartments</div>
    <div class="filter" style="top:1461px">Real Estate</div>
    <div class="filter" style="top:1532px">Hotel</div>
  </div>
  <div class="abs" style="left:316px;top:1331px;width:295px;height:184px;background:linear-gradient(180deg,#9fc7ea,#7c8a96)" role="img" aria-label="High-rise apartment towers under blue sky"></div>
  <div class="abs" style="left:611px;top:1331px;width:295px;height:184px;background:linear-gradient(180deg,#2a3444,#1d3c5c)" role="img" aria-label="Resort pool lit at night"></div>
  <svg class="abs" style="left:742px;top:1407px" width="34" height="34" aria-hidden="true">
    <circle cx="17" cy="17" r="16" fill="#fff"/>
    <path d="M12 22 L22 12" stroke="#333" stroke-width="2"/>
    <rect x="17" y="9" width="9" height="6" rx="3" transform="rotate(-45 21 12)" fill="none" stroke="#333" stroke-width="1.6"/>
    <rect x="8" y="19" width="9" height="6" rx="3" transform="rotate(-45 12 22)" fill="none" stroke="#333" stroke-width="1.6"/>
  </svg>
  <div class="abs" style="left:906px;top:1331px;width:294px;height:184px;background:linear-gradient(180deg,#d8c8a8,#6fb6c8)" role="img" aria-label="Couple walking beside a hotel pool"></div>
  <div class="abs" style="left:316px;top:1515px;width:295px;height:184px;background:linear-gradient(135deg,#d9a660,#4a3a30)" role="img" aria-label="Guest in a sunlit hotel bedroom"></div>
  <div class="abs" style="left:611px;top:1515px;width:295px;height:184px;background:linear-gradient(180deg,#1f5fb4,#1a2b4a)" role="img" aria-label="Modern apartment building illuminated at dusk"></div>
  <div class="abs" style="left:906px;top:1515px;width:294px;height:184px;background:linear-gradient(180deg,#5a9ae0,#c7d6e6)" role="img" aria-label="Building under construction with a crane"></div>
</section>

<section class="quote" role="img" aria-label="Hotel terrace and pool in evening light">
  <h2>Get A Free Quote</h2>
  <p>Lorem ipsum dolor sit amet, consectetur adipiscing elit, sed do eiusmod tempor incididunt ut labore et dolore magna aliqua.</p>
</section>
<a class="btn" style="left:512px;top:2000px;width:221px;height:60px;font-size:21px">Get A Quote</a>

<footer class="footer">
  <div class="footer-brand"><span class="brand-mark"></span>Velmorund</div>
  <h3 style="left:377px;top:38px">Links</h3>
  <div class="item" style="left:377px;top:80px">Home</div>
  <div class="item" style="left:377px;top:112px">About Us</div>
  <div class="item" style="left:377px;top:144px">Projects</div>
  <div class="item" style="left:377px;top:176px">Contact Us</div>

  <h3 style="left:537px;top:38px">Contact Us</h3>
  <svg class="abs" style="left:537px;top:86px" width="14" height="18" aria-hidden="true">
    <path d="M7 1 A5.5 5.5 0 0 1 12.5 6.5 C12.5 10 7 16 7 16 C7 16 1.5 10 1.5 6.5 A5.5 5.5 0 0 1 7 1Z" fill="none" stroke="#fff" stroke-width="1.5"/>
    <circle cx="7" cy="6.5" r="2" fill="#fff"/>
  </svg>
  <div class="item" style="left:567px;top:80px">#24, 480 Harbor Lane,<br>Coral Bay, FL 3301</div>
  <svg class="abs" style="left:536px;top:155px" width="16" height="16" aria-hidden="true">
    <path d="M3 1 L6 1 L7 5 L5 6.5 C6 9 7 10 9.5 11 L11 9 L15 10 L15 13 C15 14 14 15 13 15 C6 15 1 10 1 3 C1 2 2 1 3 1Z" fill="#fff"/>
  </svg>
  <div class="item" style="left:567px;top:150px">555-014-2876</div>
  <svg class="abs" style="left:536px;top:204px" width="17" height="13" aria-hidden="true">
    <rect x="0.75" y="0.75" width="15.5" height="11.5" fill="none" stroke="#fff" stroke-width="1.5"/>
    <path d="M1 1 L8.5 7 L16 1" fill="none" stroke="#fff" stroke-width="1.5"/>
  </svg>
  <div class="item" style="left:567px;top:196px">info@velmorundcapital.com</div>

  <h3 style="left:846px;top:38px">Newsletter</h3>
  <p class="news-text">But I must explain to you how all this mistaken idea of denouncing pleasure and praising.</p>
</footer>
<div class="news-input">Enter your email address</div>
<svg class="abs" style="left:1077px;top:2290px" width="40" height="38" aria-hidden="true">
  <rect width="40" height="38" fill="#fec214"/>
  <path d="M13 19 H26 M21 14 L26 19 L21 24" stroke="#fff" stroke-width="2" fill="none"/>
</svg>

<div class="bottom-bar">
  <div class="copyright">© 2018 Copyrights | All Rights Reserved</div>
  <span class="social" style="left:928px"></span>
  <span class="social" style="left:980px"></span>
  <span class="social" style="left:1031px"></span>
  <span class="social" style="left:1083px"></span>
</div>

</body>
</html>
```